Reliable and clean label for a natural product!

We would like to have a label design for our CBD SOFT GEL CAPSULES . We are a business family and believe in the power of natural healing. In this label we would like to show a reliable, natural and feminine product mainly.

Font styles to use
Serif
Sans Serif

Colors

Designer to choose colors to be used in the design.

```html
<!DOCTYPE html>
<html lang="en">
<head>
<meta charset="UTF-8">
<title>Verdale CBD – Soft Gel Capsules Label</title>
<link rel="stylesheet" href="https://fonts.googleapis.com/css2?family=Roboto:wght@300;400;500;700&family=Playfair+Display:wght@400&display=swap">
<style>
  :root{
    --page:#ffffff;
    --plum:#7b3f98;
    --plum-deep:#5e2a79;
    --plum-text:#6a3388;
    --lavender:#e9e3ee;
    --panel:#f7f6f8;
    --ink:#1e1a22;
    --white:#ffffff;
  }
  *{margin:0;padding:0;box-sizing:border-box}
  html,body{width:1200px;height:1200px;overflow:hidden;background:var(--page)}
  body{position:relative;font-family:"Roboto",Arial,sans-serif}

  .label{position:absolute;left:120px;top:63px;width:960px;height:1074px;overflow:hidden}
  .label-art{position:absolute;inset:0}

  .brand-mark{position:absolute;left:500px;top:6px;width:194px;height:194px;border:3px solid var(--lavender);border-radius:50%}
  .brand-name{position:absolute;left:201px;width:759px;top:232px;text-align:center;font-weight:400;font-size:110px;letter-spacing:1px;color:var(--lavender);line-height:1}

  .badges{position:absolute;left:0;top:0;width:162px;height:1074px}
  .badge{position:absolute;left:0;width:162px;text-align:center}
  .badge-icon{display:block;margin:0 auto;width:112px;height:112px;border:4px solid var(--white);border-radius:50%;background:rgba(255,255,255,.14)}
  .badge-name{display:block;margin-top:14px;font-size:20px;font-weight:500;color:var(--white);letter-spacing:.5px}

  .panel-copy{position:absolute;left:201px;width:759px;top:0;color:var(--plum-text)}
  .product-type{position:absolute;left:0;width:759px;top:462px;text-align:center;font-size:37px;font-weight:400;letter-spacing:.5px}
  .tagline{position:absolute;left:0;width:759px;top:518px;text-align:center;font-size:22px;font-weight:700;color:var(--ink)}
  .pill{position:absolute;left:224px;top:566px;width:318px;height:40px;border-radius:20px;background:var(--plum);color:var(--white);font-size:22px;font-weight:500;text-align:center;line-height:40px}
  .spectrum{position:absolute;left:0;width:759px;top:648px;text-align:center;font-size:31px;font-weight:500;line-height:1.4}
  .claims{position:absolute;left:128px;top:838px;font-size:15px;font-weight:700;color:var(--ink);line-height:1.85;text-transform:uppercase}
  .count-box{position:absolute;left:134px;top:946px;width:290px;height:40px;border:2px solid var(--plum-text);font-size:25px;font-weight:400;text-align:center;line-height:36px;color:var(--ink)}
  .net-weight{position:absolute;left:450px;top:945px;font-family:"Playfair Display",Georgia,serif;font-size:28px;color:var(--ink)}
</style>
</head>
<body>
  <section class="label">
    <svg class="label-art" width="960" height="1074" viewBox="0 0 960 1074" aria-hidden="true">
      <defs>
        <linearGradient id="plumFill" x1="0" y1="0" x2="1" y2="1">
          <stop offset="0" stop-color="#8a4aa8"/>
          <stop offset="1" stop-color="#6a3189"/>
        </linearGradient>
      </defs>
      <rect width="960" height="1074" fill="url(#plumFill)"/>
      <path d="M201,440 C360,470 470,470 620,430 C760,392 880,372 960,370 L960,1018 L201,1018 Z" fill="var(--panel)"/>
      <rect x="0" y="1040" width="960" height="4" fill="var(--lavender)" opacity=".8"/>
    </svg>

    <div class="brand-mark"></div>
    <h1 class="brand-name">VERDALE CBD</h1>

    <ul class="badges">
      <li class="badge" style="top:70px"><span class="badge-icon" role="img" aria-label="Vegan leaf icon"></span><span class="badge-name">VEGAN</span></li>
      <li class="badge" style="top:273px"><span class="badge-icon" role="img" aria-label="Vegetarian sprout icon"></span><span class="badge-name">VEGETARIAN</span></li>
      <li class="badge" style="top:460px"><span class="badge-icon" role="img" aria-label="GMO free crossed DNA icon"></span><span class="badge-name">GMO FREE</span></li>
      <li class="badge" style="top:647px"><span class="badge-icon" role="img" aria-label="Gluten free crossed wheat icon"></span><span class="badge-name">GLUTEN FREE</span></li>
      <li class="badge" style="top:837px"><span class="badge-icon" role="img" aria-label="Dairy free crossed milk bottle icon"></span><span class="badge-name">DAIRY FREE</span></li>
    </ul>

    <div class="panel-copy">
      <h2 class="product-type">CBD SOFT GEL CAPSULES</h2>
      <p class="tagline">Power Of Natural Healing</p>
      <p class="pill">Restorative Supplement</p>
      <p class="spectrum">Full Spectrum<br>25 mg CBD per capsule</p>
      <p class="claims">Complete support for the mind, body and immune system<br>GMO &amp; gluten free ingredients</p>
      <p class="count-box">30 CAPSULES</p>
      <p class="net-weight">260g e</p>
    </div>
  </section>
</body>
</html>
```